Online Training company needs a new website design (Wordpress)

We are looking for a new design for our website (run on WordPress). We currently have two websites (quizmarlow.com) and (velkorlearning.com) and are trying to combine them into a single design.

The site should contain the following sections (Start Here, courses, labs, practice exams, exam vouchers, books, articles, about us).

Start Here - With so many options on our site, we think it would be a good idea to have this page that will allow us to give students an overview of our different products/services and where to start when they first find out about our company.

Courses - These are our online video courses (products), currently hosted at velkorlearning.com. Each course has its own "product page".

Labs - These are online lab environments that a student can purchase. The layout for these would be similar to a course, but the purchase option will be different (our web developer will code all the back end stuff to make it work).

Practice Exams - This will allow students to take practice questions to study for their exams.

Exam Vouchers - Students can purchase their exam vouchers here at a discounted price for their certification exams.

Books - Will link to a page that displays our books that are available on Zorvel. (Examples of the covers are attached so you can see our current designs.)

Articles - This will be our "blog" area for us to post articles each week.

About Us - A short about us page describing our company.

***
As for the design of the page itself, we like the current color scheme at velkorlearning.com, but the layout isn't working well. It was fine when we just had video courses, but as we have added new products it is becoming more and more cumbersome.

I have been looking for inspiration around the web, and saw brightfernwealth.com as a good example of trying to provide focus to new users, while breaking out various parts of a business that contains 4-6 different product lines/topics. Another example of a site we like is lessonharborweb.com.

That said, we aren't looking to simply copy either site, and are completely open to recommendations and designs you may have.

Thank you and we look forward to working with you!

```html
<!DOCTYPE html>
<html lang="en">
<head>
<meta charset="utf-8">
<title>Online Training — Let's Develop Together</title>
<link rel="stylesheet" href="https://fonts.googleapis.com/css2?family=Montserrat:wght@400;500;600;700&display=swap">
<style>
:root{
  --navy:#1d3447;
  --navy-deep:#152838;
  --ink:#1c2a36;
  --text:#4a5560;
  --muted:#9aa3ab;
  --blue:#2aa6e0;
  --orange:#f7941d;
  --light:#f4f5f6;
  --line:#d9dde1;
  --white:#ffffff;
  --cover-top:#eef2f5;
  --cover-bottom:#d7dee4;
}
*{box-sizing:border-box;margin:0;padding:0}
html,body{width:1200px;height:5158px;overflow:hidden}
body{font-family:"Montserrat",sans-serif;color:var(--ink);background:var(--white);position:relative}
a{color:inherit;text-decoration:none}
section{position:relative;width:1200px;overflow:hidden}

.btn{display:inline-block;border-radius:20px;font-weight:600;font-size:13px;padding:11px 34px;color:var(--white);background:var(--blue)}
.btn-ghost{background:transparent;border:2px solid var(--blue);color:var(--blue);padding:12px 40px;font-size:15px}
.btn-orange{background:var(--orange)}
.btn-sm{font-size:9px;padding:5px 12px;border-radius:10px}

.section-head{text-align:center}
.section-head .kicker{font-size:22px;font-weight:500;color:var(--ink)}
.section-head .kicker::before,.section-head .kicker::after{content:"";display:inline-block;width:22px;height:2px;background:currentColor;vertical-align:middle;margin:0 10px}
.section-head h2{font-size:38px;font-weight:700;line-height:1.15}
.on-dark{color:var(--white)}
.on-dark .kicker,.on-dark h2{color:var(--white)}

.tabs{display:flex;justify-content:center;gap:22px;font-size:20px}
.tabs span{color:var(--muted)}
.tabs .active{color:var(--ink);border-bottom:2px solid var(--ink);padding-bottom:4px}

.pager{display:flex;justify-content:center;gap:20px;font-size:14px;color:var(--muted)}
.pager .current{background:#e4e7ea;color:var(--ink);width:26px;text-align:center;border-radius:3px}
.center{text-align:center}

/* header / hero */
.hero{height:567px;background:linear-gradient(180deg,#2f4a5e 0%,#1f3749 60%,#1a2e3e 100%)}
.hero .photo{position:absolute;inset:0;background:radial-gradient(ellipse at 50% 85%,rgba(120,150,170,.35),transparent 65%)}
.site-header{position:absolute;top:0;left:0;right:0;height:56px;display:flex;align-items:center;padding:0 88px;z-index:2}
.logo{font-weight:700;font-size:20px;color:var(--white)}
.nav{display:flex;gap:30px;margin-left:auto;font-size:13px;font-weight:600;color:var(--white)}
.nav .active{border-bottom:2px solid var(--blue);padding-bottom:3px}
.hero-content{position:absolute;top:176px;left:0;right:0;text-align:center;color:var(--white)}
.hero-content .kicker{font-size:26px;font-weight:500}
.hero-content .kicker::before,.hero-content .kicker::after{content:"";display:inline-block;width:24px;height:2px;background:#fff;vertical-align:middle;margin:0 12px}
.hero-content h1{font-size:50px;font-weight:700;margin-top:4px}
.hero-content p{width:560px;margin:20px auto 0;font-size:15px;line-height:1.6}
.hero-content .btn{margin-top:34px}
.arrow{position:absolute;top:262px;width:26px;height:60px;background:rgba(255,255,255,.15);display:flex;align-items:center;justify-content:center}
.arrow.left{left:0}.arrow.right{right:0}
.dots{position:absolute;top:508px;left:0;right:0;display:flex;justify-content:center;gap:12px}
.dots i{width:8px;height:8px;border-radius:50%;background:rgba(255,255,255,.45)}
.dots i.on{background:var(--blue)}

/* about */
.about{height:379px;background:var(--light);padding-top:66px}
.about p{width:760px;margin:22px auto 0;text-align:center;font-size:12.5px;line-height:1.75;color:var(--text)}
.about .btn{margin-top:28px}

/* courses */
.courses{height:739px;padding-top:82px}
.courses .tabs{margin-top:22px}
.card-row{display:flex;justify-content:center;gap:20px;margin-top:26px}
.course-card{width:234px;height:292px;background:var(--white);box-shadow:0 2px 10px rgba(0,0,0,.16)}
.course-card .thumb{height:130px;margin:6px 6px 0;position:relative;display:flex;align-items:center;justify-content:center}
.course-card h3{font-size:14px;font-weight:700;padding:14px 14px 0;line-height:1.25}
.course-card p{font-size:11px;color:var(--text);padding:8px 14px 0;line-height:1.4}
.course-card .btn{margin:14px 14px 0}
.courses .pager{margin-top:60px}
.courses .view{margin-top:42px}

/* exam banner */
.exam{height:533px;background:linear-gradient(160deg,#2b4458 0%,#1e3446 55%,#15293a 100%);clip-path:polygon(0 48px,100% 0,100% 100%,0 100%)}
.exam .section-head{padding-top:170px}
.exam p{width:600px;margin:26px auto 0;text-align:center;color:var(--white);font-size:15px;line-height:1.7}
.exam .btn{margin-top:36px}

/* vouchers */
.vouchers{height:747px;padding-top:96px}
.voucher-row{display:flex;justify-content:center;gap:86px;margin-top:48px}
.voucher{width:226px}
.voucher .badge{height:224px;border:1px solid var(--line);box-shadow:0 2px 8px rgba(0,0,0,.12);display:flex;flex-direction:column;align-items:center;justify-content:center;gap:16px}
.voucher .mark{width:110px;height:110px;border-radius:18px}
.voucher .band{width:186px;height:22px;border-top:2px solid}
.voucher .meta{display:flex;justify-content:space-between;align-items:flex-start;margin-top:18px}
.voucher h3{font-size:15px;font-weight:700;line-height:1.25}
.voucher .price{font-size:21px;font-weight:700}
.voucher p{font-size:12px;color:var(--text);line-height:1.6;margin-top:12px}
.vouchers .pager{margin-top:30px}
.vouchers .view{margin-top:36px}

/* books */
.books{height:681px;background:var(--light);clip-path:polygon(0 0,100% 42px,100% 100%,0 100%);padding-top:80px}
.book-row{display:flex;justify-content:center;gap:96px;margin-top:50px}
.book{width:220px;text-align:center}
.book .cover{width:170px;height:230px;margin:0 auto;background:linear-gradient(180deg,var(--cover-top),var(--cover-bottom));box-shadow:6px 8px 14px rgba(0,0,0,.2)}
.book h3{font-size:15px;font-weight:700;margin-top:26px}
.book h4{font-size:14px;font-weight:700}
.book p{font-size:12.5px;color:var(--text);line-height:1.55;margin-top:6px}
.books .btn{margin-top:46px}

/* articles */
.articles{height:878px;padding-top:112px}
.articles .tabs{margin-top:18px}
.article-row{display:flex;justify-content:center;gap:36px;margin-top:30px}
.article{width:270px;height:361px;background:var(--white);box-shadow:0 2px 10px rgba(0,0,0,.16)}
.article .thumb{height:150px;margin:6px;position:relative}
.article .thumb .cat{position:absolute;top:6px;left:6px;width:24px;height:24px;background:var(--blue)}
.article .thumb h3{position:absolute;left:10px;bottom:12px;font-size:17px;font-weight:700;color:var(--white)}
.article p{font-size:12.5px;color:var(--text);line-height:1.6;padding:8px 16px 0}
.article .btn{margin:14px 16px 0}
.articles .pager{margin-top:64px}
.articles .view{margin-top:52px}

/* newsletter + footer */
.footer{height:634px;background:linear-gradient(160deg,#22394b 0%,#1a2f40 60%,#132636 100%);clip-path:polygon(0 40px,100% 0,100% 100%,0 100%);padding-top:128px}
.signup{display:flex;justify-content:center;gap:28px;margin-top:42px}
.signup span{width:402px;height:50px;border:1px solid rgba(255,255,255,.7);color:var(--white);font-size:13px;font-weight:600;display:flex;align-items:center;padding-left:16px}
.footer .btn-ghost{margin-top:32px;padding:11px 44px;font-size:14px}
.cols{display:flex;justify-content:center;gap:112px;margin-top:58px;color:var(--white)}
.cols div{width:120px}
.cols h5{font-size:13px;font-weight:700;margin-bottom:8px}
.cols li{list-style:none;font-size:11px;line-height:1.55;color:#d5dde4}
</style>
</head>
<body>

<section class="hero">
  <div class="photo" role="img" aria-label="Background photo of a large audience at a conference, in dark blue tones"></div>
  <header class="site-header">
    <a class="logo" href="#">YourNiceLogo</a>
    <nav class="nav">
      <a href="#">Start Here</a><a class="active" href="#">Courses</a><a href="#">Labs</a><a href="#">Practice Exams</a><a href="#">Exam Vouchers</a><a href="#">Books</a><a href="#">Articles</a><a href="#">About us</a>
    </nav>
  </header>
  <span class="arrow left"><svg width="10" height="18" viewBox="0 0 10 18"><path d="M8 1 1 9l7 8" fill="none" stroke="#fff" stroke-width="2"/></svg></span>
  <span class="arrow right"><svg width="10" height="18" viewBox="0 0 10 18"><path d="M2 1l7 8-7 8" fill="none" stroke="#fff" stroke-width="2"/></svg></span>
  <div class="hero-content">
    <div class="kicker">Join Our Community</div>
    <h1>Let’s Develop Together</h1>
    <p>Lorem ipsum dolor sit amet, consectetuer adipiscing elit. Aenean commodo ligula eget dolor. Aenean massa. Cum sociis natoque</p>
    <a class="btn btn-ghost" href="#">Start Here</a>
  </div>
  <div class="dots"><i></i><i></i><i class="on"></i><i></i></div>
</section>

<section class="about">
  <div class="section-head"><div class="kicker">Little bit About</div><h2>Our Company</h2></div>
  <p>Lorem ipsum dolor sit amet, consectetuer adipiscing elit. Aenean commodo ligula eget dolor. Aenean massa. Cum sociis natoque penatibus et magnis dis parturient montes, nascetur ridiculus mus. Donec quam felis, ultricies nec, pellentesque eu, pretium quis, sem. Nulla consequat massa quis enim.</p>
  <div class="center"><a class="btn" href="#">Read More</a></div>
</section>

<section class="courses">
  <div class="section-head"><div class="kicker">Prepared with Experts</div><h2>Courses and Labs</h2></div>
  <div class="tabs"><span class="active">Courses</span><span>Labs</span></div>
  <div class="card-row">
    <article class="course-card">
      <div class="thumb" role="img" aria-label="Course photo of a workstation with a certification badge" style="background:linear-gradient(135deg,#24384a,#3d5568)"><svg width="62" height="62"><circle cx="31" cy="31" r="29" fill="#c8d0d8"/></svg></div>
      <h3>Certavia NetPro Practice Labs</h3><p>12 Months of hands-on virtual practice labs</p><a class="btn btn-sm" href="#">Read More</a>
    </article>
    <article class="course-card">
      <div class="thumb" role="img" aria-label="Course photo of hands working on a laptop" style="background:linear-gradient(135deg,#8fb4c6,#5e8ea6)"></div>
      <h3>Certavia NetPro Practice Labs</h3><p>12 Months of hands-on virtual practice labs</p><a class="btn btn-sm" href="#">Read More</a>
    </article>
    <article class="course-card">
      <div class="thumb" role="img" aria-label="Course illustration of a wireless network icon on a dark screen" style="background:#101820"><svg width="80" height="70" viewBox="0 0 80 70"><rect x="4" y="4" width="72" height="62" rx="8" fill="none" stroke="#2aa6e0" stroke-width="3"/><path d="M22 34a26 26 0 0 1 36 0M28 41a17 17 0 0 1 24 0" fill="none" stroke="#fff" stroke-width="4"/><circle cx="40" cy="50" r="4" fill="#fff"/></svg></div>
      <h3>Certavia NetPro Practice Labs</h3><p>12 Months of hands-on virtual practice labs</p><a class="btn btn-sm" href="#">Read More</a>
    </article>
    <article class="course-card">
      <div class="thumb" role="img" aria-label="Course photo of a desk with a certification badge" style="background:linear-gradient(135deg,#6f7d88,#3c4a56)"><svg width="62" height="62"><rect x="4" y="4" width="54" height="54" fill="#e3e8ec"/></svg></div>
      <h3>Certavia NetPro Practice Labs</h3><p>12 Months of hands-on virtual practice labs</p><a class="btn btn-sm" href="#">Read More</a>
    </article>
  </div>
  <div class="pager"><span>1</span><span class="current">2</span><span>3</span><span>4</span></div>
  <div class="center view"><a class="btn" href="#">View All</a></div>
</section>

<section class="exam" role="img" aria-label="Background photo of a student writing an exam, in dark blue tones">
  <div class="section-head on-dark"><div class="kicker">Feel Ready for Certificate</div><h2>Take One of Our Exams</h2></div>
  <p>Take one of our exams and study with practice question answering. Get a points for your answers and know your level</p>
  <div class="center"><a class="btn btn-ghost" href="#">Take Exam</a></div>
</section>

<section class="vouchers">
  <div class="section-head"><div class="kicker">Get it Here</div><h2>Exam Vouchers</h2></div>
  <div class="voucher-row">
    <div class="voucher">
      <div class="badge"><span class="mark" style="background:#6b2f86"></span><span class="band" style="border-color:#6b2f86"></span></div>
      <div class="meta"><h3>Servora Foundation<br>(Exam Voucher)</h3><span class="price">$299</span></div>
      <p>Purchase your discounted Servora foundation exam directly from Velkor training</p>
    </div>
    <div class="voucher">
      <div class="badge"><span class="mark" style="background:#2c3f8e"></span><span class="band" style="border-color:#2c3f8e"></span></div>
      <div class="meta"><h3>Servora Foundation<br>(Exam Voucher)</h3><span class="price">$299</span></div>
      <p>Purchase your discounted Servora foundation exam directly from Velkor training</p>
    </div>
    <div class="voucher">
      <div class="badge"><span class="mark" style="background:#6b2f86"></span><span class="band" style="border-color:#6b2f86"></span></div>
      <div class="meta"><h3>Servora Foundation<br>(Exam Voucher)</h3><span class="price">$299</span></div>
      <p>Purchase your discounted Servora foundation exam directly from Velkor training</p>
    </div>
  </div>
  <div class="pager"><span>1</span><span class="current">2</span><span>3</span><span>4</span></div>
  <div class="center view"><a class="btn" href="#">View All</a></div>
</section>

<section class="books">
  <div class="section-head"><div class="kicker">Our Books</div><h2>Available on Zorvel</h2></div>
  <div class="book-row">
    <div class="book"><div class="cover" role="img" aria-label="Book cover for a Servora foundation study guide"></div><h3>Book Name</h3><h4>Book Author</h4><p>Some Random Text for Representation of this Book which Would be very useful</p></div>
    <div class="book"><div class="cover" role="img" aria-label="Book cover for a Projectra foundation study guide"></div><h3>Book Name</h3><h4>Book Author</h4><p>Some Random Text for Representation of this Book which Would be very useful</p></div>
    <div class="book"><div class="cover" role="img" aria-label="Book cover for a Servora foundation study guide"></div><h3>Book Name</h3><h4>Book Author</h4><p>Some Random Text for Representation of this Book which Would be very useful</p></div>
  </div>
  <div class="center"><a class="btn btn-orange" href="#">Look on Zorvel</a></div>
</section>

<section class="articles">
  <div class="section-head"><div class="kicker">Get Information</div><h2>Our Arcticles</h2></div>
  <div class="tabs"><span class="active">Most Popular</span><span>Recent</span></div>
  <div class="article-row">
    <article class="article">
      <div class="thumb" role="img" aria-label="Article photo of a workstation with a certification badge" style="background:linear-gradient(135deg,#3a5063,#1f3040)"><span class="cat"></span><h3>Arcticle Title Here</h3></div>
      <p>Lorem ipsum dolor sit amet, consectetuer adipiscing elit. Aenean commodo ligula eget dolor. Aenean massa. Cum sociis natoque penatibus et magnis dis parturient montes, nascetur ridiculus mus.</p><a class="btn btn-sm" href="#">Read More</a>
    </article>
    <article class="article">
      <div class="thumb" role="img" aria-label="Article photo of hands working on a laptop" style="background:linear-gradient(135deg,#9cbfcf,#5f8ea5)"><span class="cat"></span></div>
      <p>Lorem ipsum dolor sit amet, consectetuer adipiscing elit. Aenean commodo ligula eget dolor. Aenean massa. Cum sociis natoque penatibus et magnis dis parturient montes, nascetur ridiculus mus.</p><a class="btn btn-sm" href="#">Read More</a>
    </article>
    <article class="article">
      <div class="thumb" role="img" aria-label="Article illustration of a wireless network icon on a dark screen" style="background:#101820"><span class="cat"></span></div>
      <p>Lorem ipsum dolor sit amet, consectetuer adipiscing elit. Aenean commodo ligula eget dolor. Aenean massa. Cum sociis natoque penatibus et magnis dis parturient montes, nascetur ridiculus mus.</p><a class="btn btn-sm" href="#">Read More</a>
    </article>
  </div>
  <div class="pager"><span>1</span><span class="current">2</span><span>3</span><span>4</span></div>
  <div class="center view"><a class="btn" href="#">View All</a></div>
</section>

<footer class="footer" role="img" aria-label="Background photo of a desk workspace, in dark blue tones">
  <div class="section-head on-dark"><div class="kicker">Join our Community</div><h2>Subscribe to Our Newsletter</h2></div>
  <div class="signup"><span>Full Name...</span><span>Email Address...</span></div>
  <div class="center"><a class="btn btn-ghost" href="#">Subscribe</a></div>
  <div class="cols">
    <div><h5>Policy</h5><ul><li>Conditions &amp; Terms</li><li>About us</li><li>Privacy Policy</li><li>Write to us</li><li>Block Security</li></ul></div>
    <div><h5>Navigation</h5><ul><li>How it Works</li><li>Pricing Page</li><li>Try Our Tools</li><li>Sign Up</li><li>Login</li></ul></div>
    <div><h5>Policy</h5><ul><li>Conditions &amp; Terms</li><li>About us</li><li>Privacy Policy</li><li>Write to us</li><li>Block Security</li></ul></div>
    <div><h5>Contacts</h5><ul><li>Your Street Adress</li><li>Phone Numbers</li><li>Email Addresses</li><li>Working Hours</li><li>Products</li></ul></div>
  </div>
</footer>

</body>
</html>
```